Supplement Bottle Label Design and Creative Lifestyle Images

We are a medical home consumer brand and we are releasing a supplement line of products called "Velbrook Nutrition". We are in need of a supplement bottle design for our supplement line, Velbrook Nutrition. We are looking for a very appealing, simple, and clean design, but with a medical feel to it.

We would like to see designs with a black background as well as designs with a white background. Bottle size will approximately be 200cc and label will about be 7" x 2.5", but this size is subject to change.

We really like the Pirlen Nutrition design and the Gantry Lab, however, we like the medical style of Nutrition Keystones. Please reference the links below.

To start off, the title of this bottle will be "Calm-Spire". We will need all similar warning about FDA, made in USA, non-GMA, GMP, ect. Please use the formula below to start:

2 Pills per serving
Blueberry pterostilbene - 10mg
Bacopa - 150mg
Gingko Biloba - 50mg
Vinpocetine - 10mg
Alpha-GPC -150mg
TAU - 35mg

https://www.shopvarn.example/Pirlen-Nutrition/b/ref=bl_dp_s_web_48213907562?ie=UTF8&node=48213907562&field-lbr_brands_browse-bin=Pirlen+Nutrition

https://www.shopvarn.example/l/7394208156

https://www.shopvarn.example/Nutrition-Keystones/b/ref=bl_dp_s_web_86420531977?ie=UTF8&node=86420531977&field-lbr_brands_browse-bin=Nutrition+Keystones

Industry/Entity Type

Medical

```html
<!DOCTYPE html>
<html lang="en">
<head>
<meta charset="utf-8">
<title>Velbrook Nutrition – Calm-Spire Label</title>
<link rel="stylesheet" href="https://fonts.googleapis.com/css2?family=Source+Sans+3:wght@400;600&family=Montserrat:wght@800;900&family=Arimo:wght@400;700&display=swap">
<style>
  :root {
    --paper: #ffffff;
    --band: #2b2a28;
    --frame: #9b9b9b;
    --ink-light: #ffffff;
    --ink-dark: #2b2a28;
    --rule: #3a3a3a;
    --badge: #f4e10e;
    --emblem: #8f8f8f;
  }
  * { margin: 0; padding: 0; box-sizing: border-box; }
  html, body { width: 1200px; height: 521px; overflow: hidden; background: var(--paper); }
  .canvas { position: relative; width: 1200px; height: 521px; font-family: "Source Sans 3", sans-serif; }

  .spec-heading {
    position: absolute; left: 0; top: 0; width: 1200px; height: 92px;
    text-align: center; color: var(--ink-dark);
    font-size: 37px; line-height: 41px; padding-top: 2px; font-weight: 400;
  }

  .label-band { position: absolute; left: 0; top: 92px; width: 1200px; height: 429px; background: var(--band); }
  .label-frame { position: absolute; left: 18px; top: 106px; width: 1162px; height: 400px; border: 2px solid var(--frame); }
  .label-face {
    position: absolute; left: 28px; top: 118px; width: 1146px; height: 378px;
    border: 2px solid var(--ink-light); border-radius: 32px; overflow: hidden;
  }

  .emblem {
    position: absolute; left: 60px; top: 176px; width: 216px; height: 216px;
    border-radius: 50%; border: 14px solid var(--emblem);
    display: flex; align-items: center; justify-content: center;
    color: var(--ink-light); font-size: 26px; font-weight: 600;
  }

  .brand-line { position: absolute; left: 310px; top: 226px; color: var(--ink-light); font-size: 39px; font-weight: 400; }
  .product-title {
    position: absolute; left: 306px; top: 268px; color: var(--ink-light);
    font-family: "Montserrat", sans-serif; font-weight: 900; font-size: 104px; letter-spacing: -4px; line-height: 1.1;
  }
  .volume { position: absolute; left: 310px; top: 386px; color: var(--ink-light); font-size: 26px; }
  .gmp-badge { position: absolute; left: 310px; top: 446px; width: 66px; height: 48px; background: var(--badge); }

  .facts-panel {
    position: absolute; left: 933px; top: 118px; width: 241px; height: 378px;
    background: var(--paper); border-radius: 0 32px 32px 0; padding: 22px 12px 0 13px; color: var(--ink-dark);
  }
  .facts-brand { font-size: 15px; line-height: 16px; }
  .facts-title { font-family: "Montserrat", sans-serif; font-weight: 800; font-size: 25px; letter-spacing: -0.5px; line-height: 28px; }
  .formula { list-style: none; width: 170px; margin-top: 6px; }
  .formula li { font-size: 12.5px; line-height: 20px; height: 21px; border-bottom: 1px solid var(--rule); }
  .formula li:last-child { border-bottom: none; }
  .notice {
    font-family: "Arimo", sans-serif; font-size: 8.3px; line-height: 9.5px;
    text-align: justify; margin-top: 9px; width: 216px;
  }
  .notice strong { font-weight: 700; }
  .formula + .notice { margin-top: 6px; }
</style>
</head>
<body>
<div class="canvas">
  <header class="spec-heading">
    <p>Velbrook Nutrition Lable</p>
    <p>Size : 7 x 2.5"</p>
  </header>

  <div class="label-band"></div>
  <div class="label-frame"></div>

  <section class="label-face">
  </section>

  <div class="emblem">Velbrook</div>

  <p class="brand-line">Velbrook Nutrition</p>
  <h1 class="product-title">Calm-Spire</h1>
  <p class="volume">200cc</p>
  <div class="gmp-badge" role="img" aria-label="Certification badge"></div>

  <aside class="facts-panel">
    <p class="facts-brand">Velbrook Nutrition</p>
    <h2 class="facts-title">Calm-Spire</h2>
    <ul class="formula">
      <li>2 Pills per serving</li>
      <li>Blueberry pterostilbene - 10mg</li>
      <li>Bacopa - 150mg</li>
      <li>Gingko Biloba - 50mg</li>
      <li>Vinpocetine - 10mg</li>
      <li>Alpha-GPC -150mg</li>
      <li>TAU - 35mg</li>
    </ul>
    <p class="notice"><strong>SUGGESTED USE :</strong> As a Dietary Supplement adults take 1 Liquid softgel daily on an empty stomach or as directed by a healthcare professional.</p>
    <p class="notice"><strong>THIS PRODUCT DOES NOT CONTAIN :</strong> Gluten, Diary, Egg, Peanut, Fish, Soy, Shellfish, Wheat, Yeast.</p>
    <p class="notice"><strong>USAGE WARNINGS :</strong> Keep out of reach of children and pets. Do not use if safety seal is damaged or missing.</p>
  </aside>
</div>
</body>
</html>
```